Business card design for strategy and management consulting company. Would like to have a clean and professional business card, based on the attached logo. The company is a strategy and management consulting company focusing on sustainable business modlels based on economic, social and environmental market opportunities. Preferably the logo should be included on both sides of the design.

Industry/Entity Type

Business

Contact Information for Business Card

Halvor Brekkeli, CEO/Management consultant
halvor.brekkeli@morvikpartners.example
Mob: +47 936 28 417
Office: Lyngvedens gate 14, pb 312 sentrum, N-0158 Oslo Norway

Requirements
Must have
• Include attached logo
Nice to have
• Would like to have the logo on both sides
Should not have
• Many colours.

```html
<!DOCTYPE html>
<html lang="en">
<head>
<meta charset="utf-8">
<title>Morvik business card</title>
<link rel="stylesheet" href="https://fonts.googleapis.com/css2?family=Roboto:wght@400;500;700&display=swap">
<style>
  :root {
    --backdrop: #c9c9c9;
    --card: #1c1d1f;
    --white: #ffffff;
    --soft-white: #e6e6e6;
    --accent: #f5d90a;
  }
  * { margin: 0; padding: 0; box-sizing: border-box; }
  html, body { width: 1200px; height: 960px; overflow: hidden; }
  body {
    background: var(--backdrop);
    font-family: "Roboto", Arial, sans-serif;
    position: relative;
  }
  .card {
    position: absolute;
    left: 320px;
    width: 600px;
    background: var(--card);
    color: var(--white);
  }
  .card-front { top: 108px; height: 333px; }
  .card-back { top: 493px; height: 342px; }

  .wordmark {
    position: absolute;
    display: flex;
    align-items: center;
    gap: 10px;
    font-weight: 500;
    color: var(--white);
    line-height: 1;
    letter-spacing: -1px;
  }
  .wordmark-dot {
    background: var(--accent);
    border-radius: 50%;
    flex: none;
  }
  .card-front .wordmark { left: 0; right: 0; top: 118px; justify-content: center; font-size: 88px; }
  .card-front .wordmark-dot { width: 14px; height: 14px; }
  .card-back .wordmark { right: 32px; top: 42px; font-size: 62px; }
  .card-back .wordmark-dot { width: 10px; height: 10px; }

  .front-web {
    position: absolute;
    left: 0; right: 0; top: 280px;
    text-align: center;
    font-size: 14px;
    letter-spacing: 4.5px;
    color: var(--soft-white);
  }

  .holder { position: absolute; left: 33px; top: 190px; }
  .holder-name { font-size: 18px; font-weight: 700; color: var(--accent); text-transform: uppercase; }
  .holder-title { font-size: 14px; font-weight: 500; margin-top: 4px; text-transform: uppercase; }

  .divider {
    position: absolute;
    left: 33px; right: 32px; top: 242px;
    height: 1px;
    background: var(--soft-white);
  }
  .contacts {
    position: absolute; left: 33px; top: 257px;
    list-style: none;
    font-size: 14px;
    color: var(--soft-white);
  }
  .contacts li { display: flex; align-items: center; gap: 9px; height: 19.5px; }
  .contacts svg { width: 13px; height: 13px; fill: var(--accent); flex: none; }
  .address {
    position: absolute; right: 32px; top: 277px;
    text-align: right;
    font-size: 14px;
    line-height: 19px;
    color: var(--soft-white);
    font-style: normal;
  }
</style>
</head>
<body>
  <section class="card card-front">
    <div class="wordmark">Morvik<span class="wordmark-dot"></span></div>
    <p class="front-web">www.morvikpartners.example</p>
  </section>

  <section class="card card-back">
    <div class="wordmark">Morvik<span class="wordmark-dot"></span></div>
    <div class="holder">
      <p class="holder-name">Halvor Brekkeli</p>
      <p class="holder-title">CEO/Management Consultant</p>
    </div>
    <div class="divider"></div>
    <ul class="contacts">
      <li>
        <svg viewBox="0 0 13 13" aria-hidden="true"><path d="M3 0h7a1 1 0 0 1 1 1v11a1 1 0 0 1-1 1H3a1 1 0 0 1-1-1V1a1 1 0 0 1 1-1zm.6 1.5v8.5h5.8V1.5zM6.5 10.7a.8.8 0 1 0 0 1.6.8.8 0 0 0 0-1.6z"/></svg>
        +47 936 28 417
      </li>
      <li>
        <svg viewBox="0 0 13 13" aria-hidden="true"><path d="M0 3h13v.8L6.5 7.6 0 3.8zM0 5.2l6.5 3.8L13 5.2V11H0z"/></svg>
        halvor.brekkeli@morvikpartners.example
      </li>
      <li>
        <svg viewBox="0 0 13 13" aria-hidden="true"><path d="M6.5 0a6.5 6.5 0 1 1 0 13 6.5 6.5 0 0 1 0-13zM3 3.2c.8.4 1.5 1.2 1.3 2.2-.2.9 1 1.2 1.2 2.2.2.9-.4 1.9.2 2.7.7-.2 1.2-1.1 1.5-1.9.4-.9 1.4-1.2 1.2-2.3-.2-.8-1.3-.8-1.9-1.3-.5-.5.2-1.4-.4-1.9C5.4 2.6 4 2.5 3 3.2z"/></svg>
        www.morvikpartners.example
      </li>
    </ul>
    <address class="address">Lyngvedens gate 14<br>pb 312 sentrum, Oslo Norway</address>
  </section>
</body>
</html>
```